Quick Straightforward Billboard Redesign

- Design billboard sized for 10 foot' x 36' foot width live area size and please include bleeds 6" around all sides
- Exact blue color match is imperative in headline, logo, phone number bubble or wherever used. C-83 / M-45 / Y-1 / K-0-
- What I hope to illustrate is that our company offers the best porch screening in the area area, in regards to quality, expertise, durability, storms proof, but we do not build screen porches.
- Current board is attached below from previous designer, and as you can see sizing was off, white space on edges make it appear to be sized incorrectly.
- I also attached my own little mock up idea well well if it helps, favorite image, logo, headline, etc and ideas perhaps on expanding or making this better?

Thanks so much!

Target Market(s)

Drivers and passengers, Southeastern NC, are of immense new construction and high end homes.

Industry/Entity Type

Construction

Colors
0054AA
0677BA
7BADD7
CADEEF
E8F1F8

Requirements
Must have
• Blue color matching
Nice to have
• Design spins or other thoughts on my little mock up

```html
<!DOCTYPE html>
<html lang="en">
<head>
<meta charset="utf-8">
<title>Tidewater Screens – Billboard</title>
<link rel="stylesheet" href="https://fonts.googleapis.com/css2?family=Antonio:wght@600;700&display=swap">
<style>
  :root {
    --brand-blue: #0054AA;
    --brand-green: #1BA44A;
    --sky-blue: #7BADD7;
    --paper: #EFF0F0;
    --stage: #E4E4E4;
  }
  html, body {
    margin: 0;
    width: 1200px;
    height: 900px;
    overflow: hidden;
    background: var(--stage);
  }
  .billboard {
    position: absolute;
    left: 40px;
    top: 295px;
    width: 1120px;
    height: 311px;
    background: var(--paper);
    overflow: hidden;
    font-family: "Antonio", "Arial Narrow", sans-serif;
  }
  .porch-photo {
    position: absolute;
    left: 0;
    top: 0;
    width: 400px;
    height: 100%;
    background:
      linear-gradient(90deg, rgba(239,240,240,0) 55%, var(--paper) 100%),
      linear-gradient(180deg, #f4f6f7 0%, #dfe6ea 28%, #8fb1cf 40%, #5f8a4c 52%, #6e6355 68%, #b9b6ad 100%);
  }
  .phone-bubble {
    position: absolute;
    left: 0;
    top: 0;
    width: 320px;
    height: 88px;
    background: var(--brand-blue);
    border-bottom-right-radius: 70px 88px;
    display: flex;
    align-items: center;
    padding-left: 24px;
    box-sizing: border-box;
    color: #fff;
    font-weight: 700;
    font-size: 50px;
    letter-spacing: 0.5px;
    white-space: nowrap;
  }
  .message {
    position: absolute;
    left: 530px;
    right: 20px;
    top: 0;
    bottom: 0;
    display: flex;
    flex-direction: column;
    justify-content: center;
  }
  .brand-name {
    display: flex;
    align-items: center;
    gap: 12px;
    color: var(--brand-blue);
    font-weight: 700;
    font-size: 40px;
    line-height: 1;
    text-transform: uppercase;
    white-space: nowrap;
    margin-bottom: 14px;
  }
  .brand-mark {
    width: 30px;
    height: 30px;
    background: var(--brand-blue);
  }
  .headline {
    margin: 0;
    font-weight: 700;
    font-size: 78px;
    line-height: 1.05;
    letter-spacing: -0.5px;
    white-space: nowrap;
  }
  .headline-primary { color: var(--brand-blue); display: block; }
  .headline-secondary { color: var(--brand-green); display: block; }
</style>
</head>
<body>
  <section class="billboard">
    <div class="porch-photo" role="img" aria-label="Screened coastal porch with wicker seating overlooking a lawn and pond"></div>
    <div class="phone-bubble">555.014.0237</div>
    <div class="message">
      <div class="brand-name"><span class="brand-mark"></span>Tidewater Screens</div>
      <h1 class="headline">
        <span class="headline-primary">Screen Your Porch.</span>
        <span class="headline-secondary">Built for the Coast.</span>
      </h1>
    </div>
  </section>
</body>
</html>
```